Bellwyn Strategic

Business Development Consulting Firm

Target Market(s)

Federal Government, 8(a) companies, Small Businesses

Industry/Entity Type

Private Sector, US Government

Contact Information for Business Card

8(a) Program Capture, Business Development, Industry Trends & Analysis, Strategic Teaming, Cyber Solutions

Colors

Designer to choose colors to be used in the design.

```html
<!DOCTYPE html>
<html lang="en">
<head>
<meta charset="utf-8">
<title>Bellwyn Strategic — Business Card</title>
<link href="https://fonts.googleapis.com/css2?family=Fira+Sans:wght@400;500;600;700&display=swap" rel="stylesheet">
<style>
  :root {
    --page: #efefef;
    --card: #232629;
    --card-soft: #3a3d40;
    --red: #d3202b;
    --red-dark: #1c1e21;
    --white: #ffffff;
    --text: #f2f2f2;
  }
  * { box-sizing: border-box; margin: 0; padding: 0; }
  html, body {
    width: 1200px; height: 1200px; overflow: hidden;
    background: var(--page);
    font-family: "Fira Sans", sans-serif;
    color: var(--text);
  }
  .canvas { position: relative; width: 1200px; height: 1200px; }

  .card {
    position: absolute; left: 262px;
    width: 674px; height: 374px;
    background: var(--card);
    border-radius: 8px; overflow: hidden;
  }
  .card--front { top: 184px; }
  .card--back { top: 626px; }

  .brand-decoration {
    position: absolute;
    background: radial-gradient(ellipse at 50% 50%, rgba(110,112,115,.55), rgba(70,72,75,.25) 55%, rgba(35,38,41,0) 75%);
  }
  .card--front .brand-decoration { left: 0; top: 0; width: 460px; height: 374px; }
  .card--back .brand-decoration { left: 0; top: 0; width: 440px; height: 374px; opacity: .45; }

  .band {
    position: absolute; left: 0; width: 100%;
    background: var(--red);
  }
  .card--front .band { top: 262px; height: 71px; }
  .card--back .band { top: 291px; height: 43px; }
  .band__cuts { position: absolute; inset: 0; }

  .company-name {
    position: absolute; left: 0; top: 262px; width: 100%; height: 71px;
    display: flex; align-items: center; justify-content: center;
    padding-left: 44px;
    font-weight: 700; font-size: 38px; letter-spacing: 1px;
    font-variant: small-caps; color: var(--white);
  }

  .logo-slot {
    position: absolute; left: 470px; top: 150px; width: 180px;
    display: flex; flex-direction: column; align-items: center; gap: 10px;
  }
  .logo-slot__dot { width: 64px; height: 64px; border-radius: 50%; background: var(--red); }
  .logo-slot__name {
    font-weight: 600; font-size: 22px; font-variant: small-caps;
    color: var(--white); letter-spacing: .5px;
  }

  .person-name {
    position: absolute; left: 158px; top: 52px;
    font-weight: 500; font-size: 26px; font-variant: small-caps;
    letter-spacing: 1px; color: var(--white);
  }

  .contact-rail {
    position: absolute; left: 100px; top: 159px; width: 47px; height: 168px;
    background: var(--red); border: 3px solid var(--red-dark);
    border-radius: 24px;
  }
  .contact-icon {
    position: absolute; left: 107px; width: 32px; height: 32px;
    border-radius: 50%; background: var(--card-soft);
    border: 2px solid var(--red-dark);
    display: flex; align-items: center; justify-content: center;
  }
  .contact-icon svg { width: 18px; height: 18px; fill: var(--white); }

  .contact-text {
    position: absolute; left: 158px;
    font-size: 11px; letter-spacing: .4px; color: var(--white);
    line-height: 14px;
  }
  .contact-text--phone { font-size: 12px; }
  .contact-text--location { font-variant: small-caps; font-size: 13px; }

  .services {
    position: absolute; right: 64px; top: 175px;
    text-align: right; list-style: none;
    font-weight: 500; font-size: 18px; font-variant: small-caps;
    line-height: 25px; color: var(--white); letter-spacing: .3px;
  }
</style>
</head>
<body>
<main class="canvas">

  <section class="card card--front" aria-label="Business card front">
    <div class="brand-decoration" role="img" aria-label="Faint large brand decoration"></div>
    <div class="band">
      <svg class="band__cuts" viewBox="0 0 674 71" preserveAspectRatio="none">
        <line x1="132" y1="0" x2="194" y2="71" stroke="#1c1e21" stroke-width="5"/>
        <line x1="526" y1="0" x2="587" y2="71" stroke="#1c1e21" stroke-width="5"/>
      </svg>
    </div>
    <h1 class="company-name">Bellwyn Strategic</h1>
    <div class="logo-slot">
      <span class="logo-slot__dot"></span>
      <span class="logo-slot__name">Bellwyn</span>
    </div>
  </section>

  <section class="card card--back" aria-label="Business card back">
    <div class="brand-decoration" role="img" aria-label="Faint large brand decoration"></div>
    <div class="band"></div>

    <h2 class="person-name">John Doe</h2>

    <div class="contact-rail"></div>
    <span class="contact-icon" style="top:164px">
      <svg viewBox="0 0 24 24"><path d="M6.6 10.8a15.1 15.1 0 0 0 6.6 6.6l2.2-2.2c.3-.3.7-.4 1-.2 1.1.4 2.3.6 3.6.6.6 0 1 .4 1 1V20c0 .6-.4 1-1 1A17 17 0 0 1 3 4c0-.6.4-1 1-1h3.5c.6 0 1 .4 1 1 0 1.3.2 2.5.6 3.6.1.3 0 .7-.2 1z"/></svg>
    </span>
    <span class="contact-icon" style="top:204px">
      <svg viewBox="0 0 24 24"><path d="M3 6h18v12H3z" fill="none" stroke="#fff" stroke-width="2"/><path d="M3 6l9 7 9-7"  fill="none" stroke="#fff" stroke-width="2"/></svg>
    </span>
    <span class="contact-icon" style="top:245px">
      <svg viewBox="0 0 24 24"><circle cx="12" cy="12" r="9" fill="none" stroke="#fff" stroke-width="2"/><path d="M3 12h18M12 3c3 3 3 15 0 18M12 3c-3 3-3 15 0 18" fill="none" stroke="#fff" stroke-width="1.6"/></svg>
    </span>
    <span class="contact-icon" style="top:284px">
      <svg viewBox="0 0 24 24"><path d="M12 2a7 7 0 0 0-7 7c0 5 7 13 7 13s7-8 7-13a7 7 0 0 0-7-7zm0 9.5a2.5 2.5 0 1 1 0-5 2.5 2.5 0 0 1 0 5z"/></svg>
    </span>

    <p class="contact-text contact-text--phone" style="top:173px">000 000 000</p>
    <p class="contact-text" style="top:213px">MAILADDRESS@MAIL.COM</p>
    <p class="contact-text" style="top:254px">WWW.WEBSITE.COM</p>
    <p class="contact-text contact-text--location" style="top:292px">Location</p>

    <ul class="services">
      <li>Program Capture</li>
      <li>Business Development</li>
      <li>Industry Trends &amp; Analysis</li>
      <li>Strategic Teaming</li>
    </ul>
  </section>

</main>
</body>
</html>
```